Business Card Design

We need a Business card design for our Family Dental Clinic.
Logo design attached.
Colour choices - White, blue and golden to go with the logo.
Business
Contact Information for Business Card
Side 1
DR MARLA FENWICKE
BDS
Suite 6, Level 2, 418 Pembury Street
Eastbrookvale, VIC 3054
Fax : 7264 5039
Email: info@eastbrookvaledentalgroup.com.au
Website: eastbrookvaledentalgroup.com.au
Phone(image) - 7264 5039 (bigger size)
Please make sure that you produce 3 files with the same design
1) As per above
2) With out the Name ( i. e DR Marla Fenwicke BDS)
3) Just the card template (no texts)
Side 2
......................................... at ........................
Please give 24 hours notice if you cannot keep this appointment

```html
<!DOCTYPE html>
<html lang="en">
<head>
<meta charset="utf-8">
<title>Eastbrookvale Dental Group – Business Card</title>
<link href="https://fonts.googleapis.com/css2?family=Exo+2:wght@400;500;600&display=swap" rel="stylesheet">
<style>
  :root {
    --backdrop: #e4e6e9;
    --card: #ffffff;
    --card-shade: #f1f2f4;
    --blue: #1f4fd6;
    --blue-deep: #1339b8;
    --blue-light: #8ea8ec;
    --ink: #2a3550;
    --text-light: #ffffff;
  }
  * { margin: 0; padding: 0; box-sizing: border-box; }
  html, body { width: 1200px; height: 898px; overflow: hidden; }
  body {
    background: var(--backdrop);
    font-family: "Exo 2", Arial, sans-serif;
    position: relative;
  }
  .card {
    position: absolute;
    top: 300px;
    width: 520px;
    height: 298px;
    background: linear-gradient(180deg, var(--card) 0%, var(--card-shade) 100%);
    box-shadow: 0 8px 24px rgba(0,0,0,0.18);
    overflow: hidden;
  }
  .card--back { left: 50px; }
  .card--front { left: 630px; }

  .brand {
    display: flex;
    align-items: center;
    gap: 10px;
    color: var(--blue);
    font-weight: 500;
  }
  .brand__dot {
    width: 34px; height: 34px;
    border-radius: 50%;
    background: var(--blue);
    flex: none;
  }
  .brand__name { line-height: 1.05; letter-spacing: 0.04em; text-transform: uppercase; }
  .brand__name span { display: block; }

  .card--back .brand {
    position: absolute;
    left: 50%; top: 42%;
    transform: translate(-50%, -50%);
    font-size: 22px;
  }
  .card--back .brand__dot { width: 46px; height: 46px; }

  .appointment {
    position: absolute;
    left: 0; right: 0; bottom: 34px;
    text-align: center;
    color: var(--ink);
    font-size: 11px;
    line-height: 1.9;
    letter-spacing: 0.02em;
  }

  .card--front .bands { position: absolute; inset: 0; }
  .card--front .brand {
    position: absolute;
    left: 30px; top: 48px;
    font-size: 19px;
  }
  .card--front .brand__name span + span { font-size: 12px; letter-spacing: 0.32em; }

  .holder {
    position: absolute;
    left: 96px; top: 142px;
    color: var(--text-light);
    text-transform: uppercase;
  }
  .holder__name { font-size: 17px; font-weight: 600; letter-spacing: 0.04em; }
  .holder__role { font-size: 10px; font-weight: 500; letter-spacing: 0.08em; }

  .contact {
    position: absolute;
    left: 312px; top: 128px;
    list-style: none;
    color: var(--text-light);
    font-size: 8.5px;
    line-height: 1.6;
    letter-spacing: 0.02em;
  }
  .contact__phone { font-size: 13px; font-weight: 600; line-height: 1.4; }
</style>
</head>
<body>

<section class="card card--back" aria-label="Card back, appointment side">
  <div class="brand">
    <span class="brand__dot"></span>
    <div class="brand__name"><span>Eastbrookvale</span><span>Dental Group</span></div>
  </div>
  <div class="appointment">
    <p>........................................................ at ..............................</p>
    <p>Please give 24 hours notice if you cannot keep this appointment</p>
  </div>
</section>

<section class="card card--front" aria-label="Card front">
  <svg class="bands" width="520" height="298" viewBox="0 0 520 298" aria-hidden="true">
    <defs>
      <linearGradient id="orange-band" x1="0" y1="0" x2="1" y2="0">
        <stop offset="0" stop-color="#e46f12"/>
        <stop offset="0.6" stop-color="#f5a623"/>
        <stop offset="1" stop-color="#ea7d18"/>
      </linearGradient>
    </defs>
    <rect x="0" y="122" width="520" height="8" fill="var(--blue-light)"/>
    <rect x="0" y="130" width="520" height="60" fill="var(--blue)"/>
    <rect x="0" y="190" width="520" height="72" fill="url(#orange-band)"/>
    <polygon points="300,118 318,104 318,118" fill="var(--blue-deep)"/>
    <polygon points="300,118 508,118 490,258 278,258" fill="var(--blue)"/>
  </svg>

  <div class="brand">
    <span class="brand__dot"></span>
    <div class="brand__name"><span>Eastbrookvale</span><span>Dental Group</span></div>
  </div>

  <div class="holder">
    <div class="holder__name">Dr Marla Fenwicke</div>
    <div class="holder__role">BDS</div>
  </div>

  <ul class="contact">
    <li class="contact__phone">&#9742; 7264 5039</li>
    <li>Fax: 7264 5039</li>
    <li>info@eastbrookvaledentalgroup.com.au</li>
    <li>eastbrookvaledentalgroup.com.au</li>
    <li>Suite 6, Level 2, 418 Pembury Street</li>
    <li>Eastbrookvale, VIC 3054</li>
  </ul>
</section>

</body>
</html>
```